Brinevale Yacht Management Full Page Ad Flyer

Yacht Management Package also includes the following periodic Monthly services:

Monthly full vessel systems checklist inspections
Diver For Hull Cleaning And Inspection Of Props, Shafts, and Zincs
Interior/Exterior Detailing and scheduled washdowns
Manage Haulout
Pump-out Services
On-call Captain and Crew Services
Updates

Need more time to provide more content to designers and the printing press template file.

Target Market(s)

Vessel owners, motor yachts, sailboats from 25 feet in length up to 125 feet in length. We do not do cruise ships or yachts larger than 125 feet. Someone who has their boat docked at their house or a local marina. We also offer mobile on-site services.

```html
<!DOCTYPE html>
<html lang="en">
<head>
<meta charset="utf-8">
<title>Brinevale Yacht Management – Periodic Services</title>
<link href="https://fonts.googleapis.com/css2?family=Cinzel:wght@600&family=Dancing+Script:wght@700&family=Poppins:wght@400;500&display=swap" rel="stylesheet">
<style>
:root{
  --backdrop:#8b8b8b;
  --navy:#232a5e;
  --navy-deep:#161c44;
  --sky:#27a6de;
  --sky-light:#4fc0ee;
  --sea-dark:#1c5f80;
  --sea-mid:#2d86aa;
  --white:#ffffff;
  --ink:#1c2150;
  --bar:#0f1a2b;
}
*{margin:0;padding:0;box-sizing:border-box}
html,body{width:1200px;height:1200px;overflow:hidden;background:var(--backdrop)}
.flyer{position:absolute;left:213px;top:106px;width:765px;height:990px;overflow:hidden;background:var(--navy);font-family:"Poppins",sans-serif;color:var(--white)}
.hero-photo{position:absolute;left:0;top:0;width:765px;height:560px;
  background:linear-gradient(160deg,var(--sea-dark) 0%,var(--sea-mid) 55%,#cfe6ef 85%,#e8f3f7 100%)}
.waves{position:absolute;left:0;top:0;width:765px;height:990px}
.brand{position:absolute;left:45px;top:34px;font-family:"Cinzel",serif;font-weight:600;color:var(--white);text-align:center;width:290px}
.brand-name{font-size:46px;letter-spacing:1px;line-height:1.1}
.brand-sub{font-size:19px;letter-spacing:3.5px;border-top:1px solid var(--white);padding-top:4px;margin-top:4px}
.title-badge{position:absolute;left:32px;top:155px;width:304px;height:304px;border-radius:50%;background:linear-gradient(160deg,#1e7fd0,var(--sky-light));}
.title-badge-inner{position:absolute;left:10px;top:10px;width:284px;height:284px;border-radius:50%;background:#f2f4fa;box-shadow:0 0 0 0 transparent}
.title-badge-inner::after{content:"";position:absolute;inset:7px;border-radius:50%;border:1.5px dashed #3b8fd6}
.title{position:absolute;left:0;top:0;width:304px;text-align:center;color:var(--ink)}
.title-script{position:absolute;top:72px;width:100%;font-family:"Dancing Script",cursive;font-size:54px;color:#2279c4;line-height:1}
.title-line{position:absolute;width:100%;font-family:"Cinzel",serif;font-weight:600;line-height:1}
.title-management{top:135px;font-size:29px}
.title-periodic{top:164px;font-size:43px;color:var(--sky)}
.title-services{top:208px;font-size:25px}
.title-dots{position:absolute;top:235px;left:0;width:100%;text-align:center;font-size:0}
.title-dots i{display:inline-block;width:7px;height:7px;border-radius:50%;margin:0 2px;background:var(--navy)}
.title-dots i:nth-child(even){background:var(--sky)}
.service{position:absolute;width:220px;text-align:center}
.service-icon{display:block;margin:0 auto;width:102px;height:102px}
.service-label{font-size:18.5px;line-height:22.5px;margin-top:12px}
.divider{position:absolute;top:512px;height:366px;border-left:2px dotted rgba(255,255,255,.75)}
.contact-bar{position:absolute;left:47px;top:919px;width:670px;height:35px;border:1px solid var(--sky);border-radius:9px;background:var(--bar);display:flex;align-items:center;font-size:19px;font-weight:500}
.contact-item{display:flex;align-items:center;gap:8px;height:100%;padding-left:12px}
.contact-item+.contact-item{border-left:1px solid var(--sky)}
.contact-item svg{width:20px;height:20px;fill:none;stroke:var(--sky);stroke-width:1.6}
</style>
</head>
<body>
<main class="flyer">
  <div class="hero-photo" role="img" aria-label="Photograph of a white sport-fishing yacht cruising at speed across deep blue sea, leaving a wide white wake"></div>

  <svg class="waves" viewBox="0 0 765 990" aria-hidden="true">
    <defs>
      <linearGradient id="bodyFill" x1="0" y1="0" x2="1" y2="0.35">
        <stop offset="0.3" stop-color="#242b5e"/>
        <stop offset="0.75" stop-color="#2796d0"/>
        <stop offset="1" stop-color="#27a6de"/>
      </linearGradient>
    </defs>
    <path d="M0 405 C160 350 320 300 480 318 C620 334 700 380 765 400 L765 990 L0 990 Z" fill="#27a6de"/>
    <path d="M300 345 C430 360 560 470 765 420" stroke="#16204a" stroke-width="11" fill="none"/>
    <path d="M0 410 C170 360 330 400 470 470 C590 520 700 500 765 420 L765 990 L0 990 Z" fill="url(#bodyFill)"/>
    <path d="M0 860 C200 920 300 900 470 990 L0 990 Z" fill="#232a5e" opacity=".5"/>
  </svg>

  <div class="brand">
    <div class="brand-name">BRINEVALE</div>
    <div class="brand-sub">YACHT MANAGEMENT</div>
  </div>

  <div class="title-badge">
    <div class="title-badge-inner"></div>
    <div class="title">
      <div class="title-script">Yacht</div>
      <div class="title-line title-management">MANAGEMENT</div>
      <div class="title-line title-periodic">PERIODIC</div>
      <div class="title-line title-services">SERVICES</div>
      <div class="title-dots"><i></i><i></i><i></i><i></i></div>
    </div>
  </div>

  <div class="divider" style="left:256px"></div>
  <div class="divider" style="left:503px"></div>

  <section class="service" style="left:33px;top:508px">
    <svg class="service-icon" viewBox="0 0 100 100" fill="none" stroke="#fff" stroke-width="2">
      <circle cx="50" cy="50" r="48" stroke-width="2.5"/><circle cx="50" cy="50" r="44" fill="#27a6de" stroke="none"/>
      <rect x="30" y="24" width="34" height="48"/><path d="M64 28l6 2-8 42"/>
      <path d="M34 34l3 3 5-5M34 44l3 3 5-5M34 54l3 3 5-5M34 64l3 3 5-5M46 35h14M46 45h14M46 55h14M46 65h14"/>
    </svg>
    <p class="service-label">Monthly full vessel<br>systems checklist<br>inspections</p>
  </section>

  <section class="service" style="left:264px;top:508px">
    <svg class="service-icon" viewBox="0 0 100 100" fill="none" stroke="#fff" stroke-width="2.2">
      <circle cx="50" cy="50" r="48" stroke-width="2.5"/><circle cx="50" cy="50" r="44" fill="#27a6de" stroke="none"/>
      <path d="M30 30l40 40M70 30L30 70"/>
      <rect x="24" y="22" width="12" height="12" transform="rotate(45 30 28)"/><rect x="64" y="66" width="12" height="12" transform="rotate(45 70 72)"/>
      <rect x="64" y="22" width="12" height="12" transform="rotate(45 70 28)"/><rect x="24" y="66" width="12" height="12" transform="rotate(45 30 72)"/>
    </svg>
    <p class="service-label">Diver For Hull<br>Cleaning And<br>Inspection Of Props,<br>Shafts, and Zincs</p>
  </section>

  <section class="service" style="left:502px;top:508px">
    <svg class="service-icon" viewBox="0 0 100 100" fill="none" stroke="#fff" stroke-width="2">
      <circle cx="50" cy="50" r="48" stroke-width="2.5"/><circle cx="50" cy="50" r="44" fill="#27a6de" stroke="none"/>
      <path d="M18 54h62l-6 12H30z"/><path d="M34 54v-8h36v8M44 46v-7h20v7M56 39v-10"/><path d="M40 50h4M48 50h4M56 50h4M64 50h4"/>
    </svg>
    <p class="service-label">Interior/Exterior<br>Detailing and<br>scheduled<br>washdowns</p>
  </section>

  <section class="service" style="left:33px;top:728px">
    <svg class="service-icon" viewBox="0 0 100 100" fill="none" stroke="#fff" stroke-width="2">
      <circle cx="50" cy="50" r="48" stroke-width="2.5"/><circle cx="50" cy="50" r="44" fill="#27a6de" stroke="none"/>
      <circle cx="50" cy="50" r="20"/><circle cx="50" cy="50" r="14"/><circle cx="50" cy="50" r="4"/>
      <path d="M50 22v56M22 50h56"/>
    </svg>
    <p class="service-label">Manage Haulout</p>
  </section>

  <section class="service" style="left:264px;top:728px">
    <svg class="service-icon" viewBox="0 0 100 100" fill="none" stroke="#fff" stroke-width="2">
      <circle cx="50" cy="50" r="48" stroke-width="2.5"/><circle cx="50" cy="50" r="44" fill="#27a6de" stroke="none"/>
      <path d="M30 36c0-10 40-10 40 0l-4 6H34z"/><path d="M34 42h32"/><path d="M47 32h6"/>
      <path d="M28 74v-10c0-6 8-10 22-10s22 4 22 10v10z"/>
    </svg>
    <p class="service-label">On-call Captain and<br>Crew Services</p>
  </section>

  <section class="service" style="left:502px;top:728px">
    <svg class="service-icon" viewBox="0 0 100 100" fill="none" stroke="#fff" stroke-width="2">
      <circle cx="50" cy="50" r="48" stroke-width="2.5"/><circle cx="50" cy="50" r="44" fill="#27a6de" stroke="none"/>
      <rect x="34" y="22" width="26" height="48" rx="2"/><rect x="38" y="27" width="18" height="10"/>
      <circle cx="47" cy="52" r="7"/><path d="M28 72h38M60 34l8 6v22c0 4 6 4 6 0V32"/>
    </svg>
    <p class="service-label">Pump-out Services</p>
  </section>

  <div class="contact-bar">
    <div class="contact-item" style="width:209px">
      <svg viewBox="0 0 24 24"><path d="M5 3l4 1 1 5-2 2c1 3 3 5 6 6l2-2 5 1 1 4c-1 2-3 2-4 2C10 22 2 14 2 6c0-1 1-3 3-3z"/></svg>+31 6 24681357
    </div>
    <div class="contact-item" style="width:218px">
      <svg viewBox="0 0 24 24"><circle cx="12" cy="12" r="9"/><path d="M3 12h18M12 3c-5 5-5 13 0 18M12 3c5 5 5 13 0 18"/></svg>www.brinevale.nl
    </div>
    <div class="contact-item">
      <svg viewBox="0 0 24 24"><rect x="2" y="5" width="20" height="14"/><path d="M2 5l10 8 10-8"/></svg>info@brinevale.nl
    </div>
  </div>
</main>
</body>
</html>
```